以前にロゴを作成頂いておりますので、そちらは使用していただきたいと思います。なお、絵と文字の部分は、分けて使用していただいたり、サイズの変更や、それぞれを単独で使用していただいたりなど、構いません。

募集の概要としては、おおむね以下のような感じです

タイトル 自宅で楽しもう!オンラインフラメンコ講習会
開催日程 全3日 各90分間(全回、同内容。参加者入替制)
①令和2年 月 日 AM :
②令和2年 月 日 PM :
③令和2年 月 日 AM :
開始時間 (いまは未定)
開催場所 ご自宅等(要WIFI環境)
講師   楠木沙也(現役若手フラメンコダンサー)
講習内容 セビジャーナス(短い入門曲をやります)
終了後は、お手本動画を参加者全員にプレゼント
参加費  無料
参加要件 ミートルーム及びトークリンク等のアプリを使用。動きやすい服装、飲み物
年齢・性別不問
定員   各回7名程度 先着順
参加方法 事前にメールにてお問い合わせ下さい(締切 開催日1週間前)
連絡先  湘陽ダンスサークルそらりお事務局
(湘陽市市民活動 登録団体)
メール  kx52614@hoshimail-demo.jp
ホームページ  https://ydssorario.pagesite-demo.com/(QRコードも載せる)

補助事業 湘陽市 まちつなぐ地域活動助成金交付事業

思いつくキーワードとしては、仲間、ストレス解消、リフレッシュ、インナーマッスル、健康、軽度の運動、姿勢、自宅で運動、楽しく踊り、オンラインでコミュニティ、気軽に携帯やPCで参加、3密ならない、靴も履かず靴下で、忙しい方、ちがう自分、軽く汗をかこう、など。使用するかしないかはもちろんお任せします。

あとは、ロゴや、過去の写真など、参考までに添付いたしますので、使用する場合は使用してください。もちろん使用しなくてもかまいませんし、おまかせいたします。

今のところは、コロナのステイホーム期間なので、自宅で運動といったようなところは入れていただきたいです。

ただ、今後、コロナの終息状況によっては、コロナという文言があてはまらなくなる可能性もあるので、当方で状況を見て、文字をこちらでなおすことができるほうがよいと考えています。(イラストレータは自宅PCで使用できますが、まだ素人レベルです)

コロナがもし終息した後も、本事業自体が不開催となることはないので、触れつつもあまりにコロナにこだわりすぎず、オンラインにより、今までお教室等がなくて参加が難しかった方々の運動や、コミュニティの形成の機会となることも、市民活動として十分意味があると考えており、一般的な内容が強くてもいいのかな、という感じです。一方で、3回だけで継続するわけでもないので、ちょっと自分でもあいまいで、イメージが出来てませんが、このあたり、出来上がったものを見ての判断かと思います。

特に特定の年齢層等をターゲットとしておらず、現在、講習を習っている方は、主婦の40代~60代の方が多いでので、社会人以上の年齢層で、一般の女性を対象となるような形であればよいと思います。男性はあまり興味がないようで、通常どこの教室も少ないので、女性対象でよいです。

限定ではないですが、湘陽市の事業なので、湘陽市民を優先する形です。

必要な場合は、ホームページの文言やキャッチコピー等、使っていただいてもかまいません。

上記記載
A4
片面
シンプル 複雑
単色 カラフル
暗い 明るい
日常 高級
遊び心 厳粛
未来的 伝統的
女性的 男性的
赤系、緑系
• 高解像度JPG (.jpg)
• イラストレーター形式 (.ai)
ポスター、チラシ等、すぐに印刷会社に依頼が掛けられるような形でお願いします。そういったこともやったことがないので、印刷の色とか、そういったものに指定があるのであれば教えて頂ければと思います。
タイトル変更のみです
日程について

①7/25(土) 14:00~
②8/9(日)  19:00~
③8/23(日) 14:00~

でお願いします。

情報量の多さと、一般市民にすんなり受け入れられるというポイントについて、すっきりとした読むのに苦労のないデザインと、踊り手の魅力が嫌みなく、自然と受け入れられるようなデザインということで決めました。色使いの綺麗さなども気に入りました。また、埋没しがちな行政関係のチラシの中でも、すっきりと、それでいてインパクトもあり、講師も同意見であったため、こちらに決定させていただきました。

今回で二回目となります。
全回に引き続き、様々な素晴らしいご提案の数々を頂き、すべてのランサー様に感謝申し上げます。
こちらが出していない写真など、一歩先までこちらのニーズを捉えてくれようという方々も多くいらっしゃったことが、ありがたかったのと、うれしかったです。
見せ方や、主張したいポイントなどがそれぞれ違い、こちらの企画の趣旨が少しでも違えば、選択も変わっていたかもしれないと思います。それぞれに個性や、特徴があり、甲乙つけがたいものがありました。
今回ご提案頂いた方々、本当にありがとうございました。

```html
<!DOCTYPE html>
<html lang="ja">
<head>
<meta charset="utf-8">
<title>自宅で楽しもう！オンラインフラメンコ講習会</title>
<link rel="stylesheet" href="https://fonts.googleapis.com/css2?family=Noto+Sans+JP:wght@400;700;900&family=M+PLUS+Rounded+1c:wght@700;800&family=Dancing+Script:wght@700&family=Montserrat:wght@600;700&display=swap">
<style>
  :root {
    --red: #d7182a;
    --deep-red: #a80f1f;
    --pink: #f3c9cf;
    --blush: #fbe7ea;
    --ink: #2a2a2a;
    --grey: #6b6b6b;
    --paper: #ffffff;
  }
  * { box-sizing: border-box; margin: 0; padding: 0; }
  html, body { width: 848px; height: 1200px; overflow: hidden; background: var(--paper); }
  body { font-family: "Noto Sans JP", sans-serif; color: var(--ink); }
  .flyer { position: relative; width: 848px; height: 1200px; overflow: hidden; background: var(--paper); }

  .hero { position: absolute; left: 0; top: 0; width: 848px; height: 540px; }
  .collage { position: absolute; left: 0; top: 0; }
  .brand { position: absolute; left: 22px; top: 20px; display: flex; align-items: center; gap: 10px; }
  .brand-dot { width: 26px; height: 26px; border-radius: 50%; background: var(--red); }
  .brand-name { font-family: "M PLUS Rounded 1c", sans-serif; font-weight: 800; font-size: 30px; color: var(--red); letter-spacing: 2px; }
  .brand-sub { position: absolute; left: 58px; top: 58px; font-size: 13px; font-weight: 700; color: var(--red); }
  .dancer-art { position: absolute; left: 20px; top: 86px; width: 118px; height: 96px; border-radius: 6px; background: linear-gradient(135deg, #f6d2d6, #e4414f); }

  .online-badge { position: absolute; right: 40px; top: 44px; width: 150px; height: 150px; border-radius: 50%; background: var(--paper); border: 3px solid var(--red); display: flex; align-items: center; justify-content: center; text-align: center; font-family: "Montserrat", sans-serif; font-weight: 700; font-size: 23px; line-height: 1.15; color: var(--red); transform: rotate(-10deg); }

  .keywords { position: absolute; left: 22px; top: 220px; display: flex; flex-direction: column; gap: 10px; list-style: none; }
  .keyword { align-self: flex-start; background: var(--red); color: var(--paper); font-weight: 700; font-size: 20px; padding: 3px 14px; }

  .lead { position: absolute; left: 0; width: 848px; top: 538px; text-align: center; }
  .lead-sub { font-family: "M PLUS Rounded 1c", sans-serif; font-weight: 800; font-size: 44px; color: var(--red); letter-spacing: 2px; }
  .free-badge { position: absolute; right: 40px; top: 494px; width: 102px; height: 102px; border-radius: 50%; background: var(--red); color: var(--paper); display: flex; flex-direction: column; align-items: center; justify-content: center; font-weight: 900; }
  .free-badge small { font-size: 14px; }
  .free-badge strong { font-size: 31px; line-height: 1.1; }
  .title { position: absolute; left: 0; width: 848px; top: 600px; text-align: center; font-family: "M PLUS Rounded 1c", sans-serif; font-weight: 800; color: var(--red); }
  .title-main { font-size: 78px; letter-spacing: 2px; line-height: 1; }
  .title-sub { font-size: 60px; letter-spacing: 14px; line-height: 1.2; }

  .teacher-photo { position: absolute; left: 0; top: 770px; width: 250px; height: 300px; background: linear-gradient(180deg, #f1d3d6, #c21a2c 70%, #8b0f1b); }
  .teacher-name { position: absolute; left: 16px; top: 1050px; background: var(--paper); padding: 6px 10px; }
  .teacher-name .role { display: inline-block; background: var(--red); color: var(--paper); font-size: 13px; font-weight: 700; padding: 1px 6px; margin-right: 6px; }
  .teacher-name strong { font-size: 30px; font-weight: 900; color: var(--red); letter-spacing: 2px; }
  .teacher-name p { font-size: 13px; font-weight: 700; }

  .schedule { position: absolute; left: 270px; top: 758px; display: flex; align-items: center; gap: 10px; }
  .schedule-note { font-size: 17px; font-weight: 900; line-height: 1.25; color: var(--ink); margin-right: 4px; }
  .schedule-note span { display: block; font-size: 11px; font-weight: 400; }
  .date { width: 112px; height: 76px; background: var(--red); color: var(--paper); text-align: center; font-family: "Montserrat", sans-serif; font-weight: 700; padding-top: 6px; }
  .date .day { font-size: 30px; line-height: 1.1; }
  .date .time { font-size: 20px; }

  .details { position: absolute; left: 270px; top: 850px; width: 400px; border-collapse: collapse; font-size: 13px; }
  .details th { width: 74px; background: var(--red); color: var(--paper); font-weight: 700; text-align: center; padding: 5px 2px; border-bottom: 3px solid var(--paper); }
  .details td { padding: 5px 8px; border-bottom: 1px dashed var(--pink); line-height: 1.4; }
  .details td em { font-style: normal; color: var(--red); font-weight: 700; }

  .enjoy { position: absolute; left: 684px; top: 856px; width: 160px; text-align: center; font-family: "Dancing Script", cursive; font-size: 32px; line-height: 1; color: var(--red); transform: rotate(-12deg); white-space: nowrap; }
  .group-photo { position: absolute; right: 20px; top: 912px; width: 140px; height: 140px; border-radius: 8px; background: linear-gradient(160deg, #fbe7ea, #d94656); }

  .contact { position: absolute; left: 270px; top: 1070px; width: 560px; border-top: 3px solid var(--red); padding-top: 8px; font-size: 13px; line-height: 1.55; }
  .contact .label { display: inline-block; background: var(--red); color: var(--paper); font-weight: 700; padding: 0 6px; margin-right: 6px; }
  .contact strong { color: var(--red); }

  .footer { position: absolute; left: 0; bottom: 0; width: 848px; height: 34px; background: var(--red); color: var(--paper); font-size: 13px; display: flex; align-items: center; justify-content: center; gap: 20px; }
</style>
</head>
<body>
<main class="flyer">
  <section class="hero">
    <svg class="collage" width="848" height="540" viewBox="0 0 848 540" role="img" aria-label="講師と受講者がフラメンコを踊る写真のコラージュ">
      <polygon points="170,0 620,0 420,300" fill="#f3d7da"/>
      <polygon points="420,300 620,0 848,0 848,230" fill="#e9b7bf"/>
      <polygon points="180,300 420,300 300,520" fill="#cf5a66"/>
      <polygon points="420,300 848,230 848,520 560,520" fill="#f0c7cd"/>
      <polygon points="300,520 420,300 560,520" fill="#b8222f"/>
      <polygon points="170,0 420,300 180,300" fill="#ead0d3"/>
    </svg>
    <div class="brand"><span class="brand-dot"></span><span class="brand-name">そらりお</span></div>
    <p class="brand-sub">湘陽ダンスサークル</p>
    <div class="dancer-art" role="img" aria-label="フラメンコダンサーのイラスト"></div>
    <div class="online-badge">Online<br>Flamenco</div>
    <ul class="keywords">
      <li class="keyword">リフレッシュに！</li>
      <li class="keyword">運動不足に！</li>
      <li class="keyword">自宅で簡単！</li>
      <li class="keyword">気軽に楽しく！</li>
    </ul>
  </section>

  <div class="lead"><p class="lead-sub">自宅で楽しもう！</p></div>
  <div class="free-badge"><small>参加費</small><strong>無料!</strong></div>
  <h1 class="title"><span class="title-main">オンラインフラメンコ</span><br><span class="title-sub">講習会</span></h1>

  <div class="teacher-photo" role="img" aria-label="赤いドレスで踊る講師の写真"></div>
  <div class="teacher-name">
    <span class="role">講師</span><strong>楠木沙也</strong>
    <p>（現役若手フラメンコダンサー）</p>
  </div>

  <div class="schedule">
    <p class="schedule-note">全3日<br>各90分<span>（全回同内容・参加者入替制）</span></p>
    <div class="date"><div class="day">7/25</div><div class="time">14:00〜</div></div>
    <div class="date"><div class="day">8/9</div><div class="time">19:00〜</div></div>
    <div class="date"><div class="day">8/23</div><div class="time">14:00〜</div></div>
  </div>

  <table class="details">
    <tr><th>開催場所</th><td>ご自宅等（要WIFI環境）</td></tr>
    <tr><th>講習内容</th><td>セビジャーナス（短い入門曲をやります）<br>終了後は、<em>お手本動画を参加者全員にプレゼント！</em></td></tr>
    <tr><th>参加要件</th><td>ミートルーム及びトークリンク等のアプリを使用。<br>動きやすい服装、飲み物　年齢・性別不問</td></tr>
    <tr><th>定　員</th><td>各回7名程度　先着順</td></tr>
    <tr><th>参加方法</th><td>事前にメールにてお問い合わせ下さい<br>（締切 開催日1週間前）</td></tr>
  </table>

  <p class="enjoy">Let's Enjoy!</p>
  <div class="group-photo" role="img" aria-label="オンラインで踊る受講者たちの写真"></div>

  <div class="contact">
    <p><span class="label">連絡先</span><strong>湘陽ダンスサークルそらりお事務局</strong>（湘陽市市民活動 登録団体）</p>
    <p>✉ kx52614@hoshimail-demo.jp　　https://ydssorario.pagesite-demo.com/</p>
  </div>

  <footer class="footer">
    <span>補助事業　湘陽市 まちつなぐ地域活動助成金交付事業</span>
    <span>湘陽市民優先・お気軽にどうぞ</span>
  </footer>
</main>
</body>
</html>
```